I need a website for my moving company Bolt Hauling LLC. I would like the following text included in my website. I have purchased the domain bolthaulingcrew.example from siteburrow.example. I am not familiar with SEO or other techniques that help my page on search engines but would like the website to be optimized for Findora search engine. I have attached our logo below and would like it to be used in the design. The colors in the logo can be used also in the design.
Home/About Us
At Bolt Hauling LLC, we know moving. It can be difficult, stressful, and a real pain in the backside. But it doesn’t have to be! When you partner with Bolt, you get the benefits of a professional moving team that is licensed and insured for your protection along with years of experience and a dedication to providing the highest quality service, each and every time.
Our Services
We do a wide variety of local moves, including apartments, single-family homes, retirement communities, dorms, condos, and many more! Our movers are trained to protect your belongings and your home – all pieces of furniture are padded and stretch wrapped free of charge, ensuring your items and home are damage-free at the end of your move. Having added stress about packing up your home prior to moving? We’ve got you covered with our full service packing and unpacking services, too.
What You Get
When you partner with BOLT, you’ll get the best service in the industry, as well as:
* The Use of Packing & Moving Materials: The hourly rate includes the use of our dollies, ratchet straps, pads, moving tools, and property protection like floor mats, door-jamb protectors, stairwell protectors, and plenty of muscle!
• Trained, Licensed, and Insured Movers: All of our movers are highly trained to provide you with the best service, and to ensure the protection of you and your items.
• Professional: Honest, Uniformed, Nice, Knowledgeable Service is what you’ll get with every member of our moving teams.
• Custom Service for Every Move: Every move is as unique as the person or business moving. Our training and equipment allows us to customize every project to ensure the very best for every client.
Target Market(s)
Home and Business movers
Industry/Entity Type
Moving Company
Colors
Designer to choose colors to be used in the design.
Requirements
Must have
- 2 sides
Nice to have
- Colorful design with logo included.
Should not have
- animated characters

```html
<!DOCTYPE html>
<html lang="en">
<head>
<meta charset="utf-8">
<title>Bolt Hauling LLC</title>
<link rel="stylesheet" href="https://fonts.googleapis.com/css2?family=Lato:wght@300;400;700;900&family=Roboto+Slab:wght@400;700&display=swap">
<style>
:root{
  --orange:#f7941d;
  --green:#7cc242;
  --green-dark:#5f9e2c;
  --ink:#222;
  --muted:#8a8a8a;
  --cream:#fdf5ea;
  --footer:#2a2a2a;
  --footer-bottom:#1b1b1b;
  --line:#d5d5d5;
}
*{box-sizing:border-box;margin:0;padding:0}
html,body{width:1200px;height:2839px;overflow:hidden}
body{font-family:'Lato',sans-serif;color:var(--ink);background:#fff;position:relative}
.abs{position:absolute}

/* top bar */
.topbar{left:0;top:0;width:1200px;height:42px;background:var(--orange)}
.hours{left:536px;top:11px;color:#fff;font-size:15px;font-weight:700;display:flex;align-items:center;gap:8px}
.phone-tab{left:912px;top:0;width:210px;height:53px;background:var(--green);border-radius:0 0 6px 6px;color:#fff;font-size:22px;font-weight:700;display:flex;align-items:center;justify-content:center;gap:10px}

/* header */
.header{left:0;top:42px;width:1200px;height:94px;background:#fff}
.brand{display:flex;align-items:center;gap:10px;font-weight:900;font-size:20px;color:var(--orange);letter-spacing:.5px}
.brand-mark{width:18px;height:18px;background:var(--green)}
.header .brand{position:absolute;left:80px;top:34px}
.nav{position:absolute;right:74px;top:0;display:flex;gap:0;height:94px}
.nav a{display:block;padding:42px 27px 0;font-size:15px;color:#777;text-decoration:none;font-weight:300;letter-spacing:.3px;height:94px}
.nav a.active{color:var(--green);border-bottom:4px solid #333}

/* hero */
.hero{left:0;top:136px;width:1200px;height:530px;background:linear-gradient(90deg,#5d5d5d 0%,#8a8a8a 55%,#b9b9b9 100%)}
.hero-title{left:78px;top:272px;color:#fff;font-size:64px;font-weight:900;letter-spacing:-.5px}
.hero-sub{left:78px;top:347px;color:#fff;font-size:22px}
.hero-text{left:78px;top:393px;width:580px;color:#fff;font-size:16px;line-height:26px}
.btn{display:inline-flex;align-items:center;justify-content:center;background:var(--green);color:#fff;font-size:18px;font-weight:700;text-transform:uppercase;border-radius:3px;text-decoration:none}
.hero .btn,.hero-btn{left:78px;top:464px;width:145px;height:51px}

/* categories */
.cats{left:0;top:600px;width:1200px;display:flex;justify-content:center;gap:0}
.cat{width:210px;text-align:center}
.cat-icon{width:132px;height:132px;border-radius:50%;background:#fff;margin:0 auto;box-shadow:0 0 0 6px #eee;display:flex;align-items:center;justify-content:center}
.cat-art{width:88px;height:88px;border-radius:50%}
.cat h3{margin-top:40px;font-size:16px;font-weight:400;color:var(--orange);text-transform:uppercase;line-height:20px;min-height:20px}
.cat p{margin-top:6px;font-size:13.5px;line-height:20px;color:#666;padding:0 12px}

/* about */
.about{left:0;top:905px;width:1200px;height:367px;background:var(--cream)}
.about-photo{left:78px;top:962px;width:530px;height:246px;background:linear-gradient(135deg,#b98d63,#e8d7c2 45%,#6f8a4f);box-shadow:0 10px 18px rgba(0,0,0,.15)}
.eyebrow{font-family:'Lato',sans-serif;font-size:20px;color:var(--ink)}
.section-title{font-family:'Roboto Slab',serif;font-weight:700;font-size:40px;color:#111}
.about-head{left:638px;top:960px;width:370px;text-align:center}
.about-head .section-title{margin-top:2px}
.about-text{left:638px;top:1054px;width:528px;font-size:15.5px;line-height:25.5px;color:#555}

/* features */
.features-head{left:0;top:1320px;width:1200px;text-align:center}
.features-head .section-title{font-size:38px;margin-top:4px}
.features{left:78px;top:1416px;width:1048px;display:flex;gap:12px}
.feature{width:253px;text-align:center;border-top:3px solid var(--line);padding-top:26px}
.feature.active{border-color:var(--orange)}
.feature-icon{width:106px;height:106px;border-radius:50%;border:2px solid var(--orange);margin:0 auto;display:flex;align-items:center;justify-content:center;background:#fff}
.feature.active .feature-icon{background:var(--green);border:5px solid var(--green-dark)}
.feature h3{margin-top:20px;font-size:18px;font-weight:400;line-height:23px;color:var(--ink);min-height:46px}
.feature.active h3{color:var(--orange)}
.feature p{margin-top:2px;font-size:13.5px;line-height:20.5px;color:var(--muted);padding:0 10px}

/* cta */
.cta{left:0;top:1798px;width:1200px;height:428px;background:linear-gradient(90deg,#3c3c3c 0%,#5e544b 55%,#8b735c 100%)}
.cta-lead{left:78px;top:1906px;color:#fff;font-family:'Roboto Slab',serif;font-size:29px;line-height:36px}
.cta-title{left:78px;top:1993px;color:#fff;font-family:'Roboto Slab',serif;font-weight:700;font-size:45px}
.cta-btn{left:76px;top:2071px;width:146px;height:53px}

/* map */
.map{left:0;top:2226px;width:1200px;height:311px;background:linear-gradient(180deg,#eceef0,#e4e7ea)}

/* footer */
.footer{left:0;top:2537px;width:1200px;height:249px;background:var(--footer)}
.footer h4{font-family:'Roboto Slab',serif;font-weight:400;font-size:18px;color:var(--green);text-transform:uppercase}
.feed{left:78px;top:2567px;width:340px}
.post{display:flex;gap:14px;margin-top:22px}
.avatar{width:40px;height:40px;border-radius:50%;background:#8b8b8b;flex:none;border:2px solid #555}
.post-body{font-size:13.5px;line-height:19px;color:#ddd}
.post-body .when{color:var(--orange);margin-left:20px}
.post-actions{display:flex;gap:6px;margin-top:4px}
.post-actions span{border:1px solid #bbb;color:#ccc;font-size:10px;padding:1px 6px;border-radius:2px}
.footer-brand{left:480px;top:2597px;width:240px;text-align:center}
.footer-brand .brand{justify-content:center;font-size:20px;color:#fff}
.socials{display:flex;justify-content:center;gap:10px;margin-top:30px}
.socials span{width:40px;height:40px;border-radius:50%;background:#555}
.socials span:first-child{background:var(--green)}
.contact{left:792px;top:2567px;width:320px}
.contact ul{list-style:none;margin-top:18px}
.contact li{display:flex;gap:14px;color:#ddd;font-size:14px;line-height:20px;margin-bottom:18px}
.contact svg{flex:none}
.bottom{left:0;top:2786px;width:1200px;height:53px;background:var(--footer-bottom);color:#ccc;font-size:14px;display:flex;align-items:center;justify-content:center}
.bottom b{color:var(--green);margin:0 4px}
</style>
</head>
<body>

<div class="abs topbar"></div>
<div class="abs hours">
  <svg width="18" height="18" viewBox="0 0 20 20"><circle cx="10" cy="10" r="8" fill="none" stroke="#fff" stroke-width="2"/><path d="M10 5v5l3 2" stroke="#fff" stroke-width="2" fill="none"/></svg>
  Mon-Fri : 9:00AM - 5:00PM Sat-Sun : Closed
</div>
<div class="abs phone-tab">
  <svg width="20" height="20" viewBox="0 0 24 24"><path fill="#fff" d="M6.6 10.8a15.1 15.1 0 006.6 6.6l2.2-2.2c.3-.3.7-.4 1-.2 1.1.4 2.3.6 3.6.6.6 0 1 .4 1 1V20c0 .6-.4 1-1 1A17 17 0 013 4c0-.6.4-1 1-1h3.5c.6 0 1 .4 1 1 0 1.3.2 2.5.6 3.6.1.3 0 .7-.2 1z"/></svg>
  (555) 204-7781
</div>

<header class="abs header">
  <div class="brand"><span class="brand-mark"></span>BOLT HAULING</div>
  <nav class="nav">
    <a href="#" class="active">HOME</a>
    <a href="#">ABOUT</a>
    <a href="#">SERVICES</a>
    <a href="#">WHAT YOU GET</a>
    <a href="#">CONTACT</a>
  </nav>
</header>

<section class="abs hero" role="img" aria-label="Couple sitting on the floor among moving boxes in a new home"></section>
<h1 class="abs hero-title">BOLT HAULING</h1>
<p class="abs hero-sub">Making Your Moving Least Painful</p>
<p class="abs hero-text">At Bolt Hauling LLC, we know moving. It can be difficult, stressful, and a real pain in the backside. But it doesn't have to be!</p>
<a href="#" class="abs btn hero-btn">Read More</a>

<section class="abs cats">
  <div class="cat">
    <div class="cat-icon"><div class="cat-art" role="img" aria-label="Apartment tower illustration" style="background:linear-gradient(135deg,#9fc3e6,#5c86b3)"></div></div>
    <h3>Apartments</h3>
    <p>Lorem Ipsum is simply dummy text of the printing and typesetting industry.</p>
  </div>
  <div class="cat">
    <div class="cat-icon"><div class="cat-art" role="img" aria-label="Single family house illustration" style="background:linear-gradient(135deg,#f7a55a,#e0662a)"></div></div>
    <h3>Single Family<br>Homes</h3>
    <p>Lorem Ipsum is simply dummy text of the printing.</p>
  </div>
  <div class="cat">
    <div class="cat-icon"><div class="cat-art" role="img" aria-label="Retirement community door illustration" style="background:linear-gradient(135deg,#f3b94a,#6b4a2e)"></div></div>
    <h3>Retirement<br>Communities</h3>
    <p>Lorem Ipsum is simply dummy text of the printing.</p>
  </div>
  <div class="cat">
    <div class="cat-icon"><div class="cat-art" role="img" aria-label="Dormitory building illustration" style="background:linear-gradient(135deg,#c9b38e,#6e8f6a)"></div></div>
    <h3>Dorms</h3>
    <p>Lorem Ipsum is simply dummy text of the printing and typesetting industry.</p>
  </div>
  <div class="cat">
    <div class="cat-icon"><div class="cat-art" role="img" aria-label="Condo house illustration" style="background:linear-gradient(135deg,#f1c27a,#d2502e)"></div></div>
    <h3>Condos</h3>
    <p>Lorem Ipsum is simply dummy text of the printing and typesetting industry.</p>
  </div>
</section>

<section class="abs about"></section>
<div class="abs about-photo" role="img" aria-label="Two movers carrying a sofa out of a truck"></div>
<div class="abs about-head">
  <p class="eyebrow">Our Story</p>
  <h2 class="section-title">ABOUT US</h2>
</div>
<p class="abs about-text">At Bolt Hauling LLC, we know moving. It can be difficult, stressful, and a real pain in the backside. But it doesn't have to be! When you partner with Bolt, you get the benefits of a professional moving team that is licensed and insured for your protection along with years of experience and a dedication to providing the highest quality service, each and every time.</p>

<div class="abs features-head">
  <p class="eyebrow">What Makes Our Company</p>
  <h2 class="section-title">DIFFERENT &amp; BETTER?</h2>
</div>
<section class="abs features">
  <div class="feature active">
    <div class="feature-icon">
      <svg width="56" height="56" viewBox="0 0 56 56" fill="none" stroke="#fff" stroke-width="2.5" stroke-linejoin="round"><path d="M28 10l18 8v20l-18 8-18-8V18z"/><path d="M10 18l18 8 18-8M28 26v20"/><path d="M10 18l-4 7 18 8 4-7M46 18l4 7-18 8-4-7"/></svg>
    </div>
    <h3>Packing &amp; Moving<br>Materials</h3>
    <p>The hourly rate includes the use of our dollies, ratchet straps, pads, moving tools, and property protection like floor mats, door-jamb protectors, stairwell protectors, and plenty of muscle!</p>
  </div>
  <div class="feature">
    <div class="feature-icon" role="img" aria-label="Two movers carrying a box icon">
      <svg width="56" height="56" viewBox="0 0 56 56" fill="none" stroke="#666" stroke-width="2.5"><rect x="20" y="20" width="16" height="14"/><path d="M12 46V28l8-4M44 46V28l-8-4"/></svg>
    </div>
    <h3>Trained, Licensed, and<br>Insured Movers</h3>
    <p>All of our movers are highly trained to provide you with the best service, and to ensure the protection of you and your items.</p>
  </div>
  <div class="feature">
    <div class="feature-icon" role="img" aria-label="Moving truck icon">
      <svg width="56" height="56" viewBox="0 0 56 56" fill="none" stroke="#666" stroke-width="2.5"><rect x="8" y="20" width="26" height="16"/><path d="M34 25h8l6 6v5H34z"/><circle cx="16" cy="38" r="3"/><circle cx="40" cy="38" r="3"/></svg>
    </div>
    <h3>Professional</h3>
    <p>Honest, Uniformed, Nice, Knowledgeable Service is what you'll get with every member of our moving teams.</p>
  </div>
  <div class="feature">
    <div class="feature-icon">
      <svg width="56" height="56" viewBox="0 0 56 56" fill="#666"><path d="M22 12l8 4v9l-8 4-8-4v-9z"/><path d="M36 18l8 4v9l-8 4-8-4v-9z" opacity=".7"/><path d="M24 30l8 4v9l-8 4-8-4v-9z" opacity=".85"/></svg>
    </div>
    <h3>Custom Service for Every<br>Move</h3>
    <p>Every move is as unique as the person or business moving. Our training and equipment allows us to customize every project to ensure the very best for every client.</p>
  </div>
</section>

<section class="abs cta" role="img" aria-label="Smiling family unpacking cardboard boxes at home"></section>
<p class="abs cta-lead">IF you've sold your house and need to pack<br>it all and move it all to a new location,</p>
<h2 class="abs cta-title">That's When We'll Come In U.S.</h2>
<a href="#" class="abs btn cta-btn">Book Now</a>

<section class="abs map" role="img" aria-label="Street map showing the company location"></section>

<footer class="abs footer"></footer>
<div class="abs feed">
  <h4>Chatterly Feed</h4>
  <div class="post">
    <div class="avatar"></div>
    <div class="post-body">Lorem Ipsum is simply dummy <span class="when">2h ago</span><br>text of the printing.<br>2 days ago at 8:30am
      <div class="post-actions"><span>Like</span><span>Love</span></div></div>
  </div>
  <div class="post">
    <div class="avatar"></div>
    <div class="post-body">Lorem Ipsum is simply dummy <span class="when">5h ago</span><br>text of the printing.<br>2 days ago at 8:30am
      <div class="post-actions"><span>Like</span><span>Love</span></div></div>
  </div>
</div>
<div class="abs footer-brand">
  <div class="brand"><span class="brand-mark"></span>BOLT HAULING</div>
  <div class="socials"><span></span><span></span><span></span></div>
</div>
<div class="abs contact">
  <h4>Contact Info</h4>
  <ul>
    <li><svg width="20" height="24" viewBox="0 0 20 24"><path d="M10 1a8 8 0 00-8 8c0 6 8 14 8 14s8-8 8-14a8 8 0 00-8-8z" fill="none" stroke="#f7941d" stroke-width="2"/><circle cx="10" cy="9" r="3" fill="none" stroke="#f7941d" stroke-width="2"/></svg>42 Linden Row, Maple Falls,<br>ST 00000, US</li>
    <li><svg width="20" height="20" viewBox="0 0 24 24"><path fill="none" stroke="#f7941d" stroke-width="2" d="M6.6 10.8a15.1 15.1 0 006.6 6.6l2.2-2.2c.3-.3.7-.4 1-.2 1.1.4 2.3.6 3.6.6.6 0 1 .4 1 1V20c0 .6-.4 1-1 1A17 17 0 013 4c0-.6.4-1 1-1h3.5c.6 0 1 .4 1 1 0 1.3.2 2.5.6 3.6.1.3 0 .7-.2 1z"/></svg>(555) 204-7781</li>
    <li><svg width="20" height="16" viewBox="0 0 20 16"><rect x="1" y="1" width="18" height="14" fill="none" stroke="#f7941d" stroke-width="2"/><path d="M1 2l9 7 9-7" fill="none" stroke="#f7941d" stroke-width="2"/></svg>info@bolthaul.example</li>
  </ul>
</div>
<div class="abs bottom">© <b>BOLT MOVE</b> - 2017. All Rights Reserved</div>

</body>
</html>
```